Need a design for Loan Site with new age design

We need a design for our site www.credvista.in , we deal with different verticals like home loan, personal loan, loan against property and business loans. Feel free to get in touch if you have any questions.

I have like the concept of the drop down on the eye level where consumer is able to select the product they wish and continue with the form https://www.tulsiorbit.com/ . They are in the same line of business as we are.

Here are few more designs which i personally like just to get idea about the taste

https://plumridgestudio.com/
http://zenpik.com/partners

Industry/Entity Type

Loan

Number of Pages Required

2 page

Colors
34a7d7
add136
faa54b
fbee3e

Requirements
Must have
• I have like the concept of the drop down on the eye level where consumer is able to select the product they wish and continue with the form https://www.tulsiorbit.com/ . They are in the same line of business as we are.
• Here are few more designs which i personally like just to get idea about the taste
• https://plumridgestudio.com/
• http://zenpik.com/partners

```html
<!DOCTYPE html>
<html lang="en">
<head>
<meta charset="utf-8">
<title>CredVista – Secured and Unsecured Loans</title>
<link href="https://fonts.googleapis.com/css2?family=Play:wght@700&family=Open+Sans:wght@400;600&display=swap" rel="stylesheet">
<style>
:root{
  --brand:#0b5c91;
  --brand-dark:#0a2546;
  --hero-a:#1d5e8c;
  --hero-b:#3f86b3;
  --accent-red:#f25656;
  --accent-orange:#ff7a0a;
  --ink:#111;
  --muted:#4a4a4a;
  --panel:#ececec;
  --line:#d6d6d6;
  --white:#fff;
}
*{box-sizing:border-box;margin:0;padding:0}
html,body{width:940px;height:1200px;overflow:hidden;background:var(--white)}
body{font-family:"Open Sans",Arial,sans-serif;color:var(--ink);position:relative}
.site-header{position:absolute;top:0;left:0;width:940px;height:108px;background:var(--white)}
.brand{position:absolute;left:36px;top:38px;display:flex;align-items:center;gap:8px;font-weight:600;font-size:20px;color:var(--brand)}
.brand-mark{width:18px;height:18px;background:var(--brand)}
.main-nav{position:absolute;top:31px;right:22px;display:flex;gap:2px}
.main-nav a{font-family:Arial,sans-serif;font-size:13px;color:var(--ink);text-decoration:none;padding:0 14px;height:33px;line-height:33px}
.main-nav a.active{background:var(--brand);color:var(--white)}
.hero{position:absolute;top:108px;left:0;width:940px;height:364px;text-align:center;color:var(--white)}
.hero-photo{position:absolute;inset:0;background:linear-gradient(120deg,var(--hero-b),var(--hero-a) 55%,#2a6f9d)}
.hero h1{position:absolute;top:76px;width:100%;padding-left:20px;font-family:"Play",sans-serif;font-size:31px;font-weight:700;letter-spacing:.3px}
.hero .lede{position:absolute;top:116px;left:0;width:100%;padding-left:120px;font-size:24px}
.hero-arrows{position:absolute;top:164px;left:416px}
.search-bar{position:absolute;top:245px;left:282px;display:flex;gap:2px}
.select{width:162px;height:35px;background:var(--white);color:#777;font-size:12.5px;display:flex;align-items:center;justify-content:space-between;padding:0 12px 0 14px}
.search-btn{width:99px;height:35px;background:var(--accent-red);color:var(--white);font-size:17px;display:flex;align-items:center;justify-content:center}
.partners{position:absolute;top:472px;left:0;width:940px;height:206px;background:var(--panel);text-align:center}
.section-title{font-family:"Play",sans-serif;font-weight:700;font-size:28px;color:var(--ink)}
.partners .section-title{position:absolute;top:48px;width:100%;padding-left:32px}
.partner-row{position:absolute;top:103px;left:54px;display:flex;gap:8px}
.partner{width:160px;height:63px;background:var(--white);border:1px solid var(--line);display:flex;align-items:center;justify-content:center;gap:6px;font-weight:600;font-size:15px;color:var(--brand)}
.partner i{width:12px;height:12px;border-radius:50%;background:var(--brand);display:block}
.features{position:absolute;top:678px;left:0;width:940px;height:342px}
.features .section-title{position:absolute;top:40px;width:100%;text-align:center}
.feature{position:absolute;display:flex;align-items:center;gap:17px;font-size:16.6px;color:var(--muted);line-height:20px}
.feature .icon{width:76px;height:76px;border-radius:50%;background:var(--brand);display:flex;align-items:center;justify-content:center;flex:none}
.cta{position:absolute;top:1020px;left:0;width:940px;height:138px;background:var(--brand-dark);overflow:hidden}
.cta-art{position:absolute;right:0;top:0;width:340px;height:138px;background:radial-gradient(circle at 70% 40%,#2b6c93,#153866 55%,var(--brand-dark) 80%)}
.cta h2{position:absolute;top:26px;left:291px;font-family:"Play",sans-serif;font-size:28.4px;color:var(--white)}
.cta-btn{position:absolute;top:74px;left:399px;width:139px;height:35px;background:var(--accent-orange);color:var(--white);font-size:16px;font-weight:600;display:flex;align-items:center;justify-content:center}
.site-footer{position:absolute;top:1158px;left:0;width:940px;height:42px;text-align:center;line-height:42px;font-size:13.5px;color:var(--muted)}
</style>
</head>
<body>
<header class="site-header">
  <div class="brand"><span class="brand-mark"></span>CredVista</div>
  <nav class="main-nav">
    <a class="active">Home</a><a>Who we are</a><a>Services</a><a>Blog</a><a>Career</a><a>Reach us</a>
  </nav>
</header>

<section class="hero">
  <div class="hero-photo" role="img" aria-label="Photo of hands signing a loan document with a pen, tinted blue"></div>
  <h1>Looking for a Secured or Unsecured loan</h1>
  <p class="lede">We will help you Best Interest Rate</p>
  <svg class="hero-arrows" width="104" height="62" viewBox="0 0 104 62" fill="none" stroke="#fff" stroke-width="2.5" stroke-linecap="round">
    <path d="M4 8 L14 56 M6 46 L14 56 L20 44"/>
    <path d="M36 2 L38 54 M30 44 L38 54 L44 44"/>
    <path d="M64 4 L66 54 M58 44 L66 54 L72 44"/>
    <path d="M98 8 L90 56 M84 44 L90 56 L98 46"/>
  </svg>
  <div class="search-bar">
    <div class="select">I would like to <svg width="14" height="8" viewBox="0 0 14 8" fill="none" stroke="#f25656" stroke-width="1.6"><path d="M1 1 L7 7 L13 1"/></svg></div>
    <div class="select">Select a Product <svg width="14" height="8" viewBox="0 0 14 8" fill="none" stroke="#f25656" stroke-width="1.6"><path d="M1 1 L7 7 L13 1"/></svg></div>
    <div class="search-btn">Search</div>
  </div>
</section>

<section class="partners">
  <h2 class="section-title">We work with all premium financial institution</h2>
  <div class="partner-row">
    <div class="partner"><i></i>Harbourline Bank</div>
    <div class="partner"><i></i>Velquora Bank</div>
    <div class="partner"><i></i>Sundrel Bank</div>
    <div class="partner"><i></i>Zentrova Finserv</div>
    <div class="partner"><i></i>Tarvelo Bank</div>
  </div>
</section>

<section class="features">
  <h2 class="section-title">Our Features</h2>
  <div class="feature" style="left:39px;top:107px">
    <div class="icon"><svg width="36" height="34" viewBox="0 0 36 34" fill="#fff"><rect x="0" y="14" width="8" height="20" rx="1"/><path d="M11 14 L18 2 C21 0 24 2 23 6 L21 12 L32 12 C35 12 36 15 35 17 L32 31 C31 33 30 34 28 34 L11 34 Z"/></svg></div>
    <span>Get approval within 7 business days</span>
  </div>
  <div class="feature" style="left:467px;top:106px">
    <div class="icon"><span style="color:#fff;font-size:40px;font-weight:600">₹</span></div>
    <span>Doorstep deliveries</span>
  </div>
  <div class="feature" style="left:37px;top:213px">
    <div class="icon"><svg width="40" height="28" viewBox="0 0 40 28" fill="#fff"><rect x="0" y="0" width="24" height="20"/><path d="M26 6 H33 L40 14 V22 H26 Z"/><circle cx="8" cy="23" r="4.5" stroke="#0b5c91" stroke-width="2"/><circle cx="32" cy="23" r="4.5" stroke="#0b5c91" stroke-width="2"/></svg></div>
    <span>Comapre quote from all major financial<br>Institutions</span>
  </div>
  <div class="feature" style="left:468px;top:210px">
    <div class="icon"><svg width="26" height="34" viewBox="0 0 26 34"><path d="M0 0 H18 L26 8 V34 H0 Z" fill="#fff"/><path d="M5 10 H20 M5 15 H20 M5 20 H14" stroke="#0b5c91" stroke-width="2"/><circle cx="18" cy="25" r="4" fill="none" stroke="#0b5c91" stroke-width="2"/></svg></div>
    <span>Easy Documentation</span>
  </div>
</section>

<section class="cta">
  <div class="cta-art" role="img" aria-label="Illustration of communication devices: envelope, phone, tablet and microphone"></div>
  <h2>What are you waiting for?</h2>
  <div class="cta-btn">Inquire Now</div>
</section>

<footer class="site-footer">Copyright © 2016 CredVista Private Policy</footer>
</body>
</html>
```